Insurance company needs a business card design

We need a business card design for a Massachusetts-based insurance company Cielora Insurance, LLC. We provide auto insurance to Hispanic (Spanish- or Portuguese-speaking) immigrants in the United States. We will give these business cards to auto dealers where such customers typically go to purchase vehicles. We will provide a solution to the dealers to provide easy insurance to the customers buying cars at their dealerships. Cielora is the Spanish word for protection.
Contact Information for Business Card
Name, Designation, Company Name, Address, Phone Number, Email, Website
Look and feel
Each slider illustrates characteristics of the customer's brand and the style your logo design should communicate.

```html
<!DOCTYPE html>
<html lang="en">
<head>
<meta charset="utf-8">
<title>Cielora Insurance – Business Card</title>
<link href="https://fonts.googleapis.com/css2?family=Raleway:wght@500;700&family=Roboto:wght@400&display=swap" rel="stylesheet">
<style>
  :root{
    --stage:#a6a6a6;
    --navy:#024a7b;
    --orange:#f08300;
    --white:#ffffff;
    --gold:#f9c53f;
    --shadow:#1e1e1e;
  }
  html,body{margin:0;padding:0;overflow:hidden;}
  body{width:1200px;height:1125px;background:var(--stage);position:relative;font-family:"Roboto",sans-serif;}
  .card{position:absolute;left:212px;width:732px;height:442px;box-shadow:3px 3px 0 var(--shadow);overflow:hidden;}
  .card--front{top:100px;background:var(--white);}
  .card--back{top:600px;background:var(--orange);}
  .card__waves{position:absolute;inset:0;}
  .brand{position:absolute;font-family:"Raleway",sans-serif;font-weight:700;margin:0;text-transform:uppercase;line-height:1;}
  .brand--front{left:45px;top:118px;color:var(--navy);font-size:40px;letter-spacing:1px;}
  .brand--front span{display:block;font-size:20px;letter-spacing:7px;margin-top:8px;}
  .brand--back{left:0;right:0;top:190px;text-align:center;color:var(--gold);font-size:52px;letter-spacing:2px;}
  .brand--back span{display:block;font-size:24px;letter-spacing:10px;margin-top:10px;}
  .holder{position:absolute;right:52px;top:62px;text-align:right;font-family:"Raleway",sans-serif;}
  .holder__name{margin:0;color:var(--navy);font-weight:700;font-size:30px;line-height:1;}
  .holder__role{margin:6px 0 0;color:var(--orange);font-weight:500;font-size:20px;line-height:1;}
  .address{position:absolute;left:45px;top:348px;color:var(--white);font-size:19.5px;line-height:26px;margin:0;}
  .contacts{position:absolute;right:48px;top:331px;list-style:none;margin:0;padding:0;color:var(--white);font-size:19.5px;}
  .contacts li{display:flex;align-items:center;justify-content:flex-end;height:26.5px;letter-spacing:.3px;}
  .contacts svg{width:19px;height:19px;margin-left:8px;flex:none;}
</style>
</head>
<body>
  <section class="card card--front">
    <svg class="card__waves" viewBox="0 0 732 442" aria-hidden="true">
      <path d="M0 228 C150 305 400 330 732 158 L732 442 L0 442 Z" fill="var(--navy)"/>
      <path d="M49 246 C250 318 480 300 732 108 L732 146 C480 312 250 322 49 246 Z" fill="var(--orange)"/>
    </svg>
    <h1 class="brand brand--front">Cielora<span>Insurance</span></h1>
    <div class="holder">
      <p class="holder__name">Daniel Reyes</p>
      <p class="holder__role">Managing Director</p>
    </div>
    <p class="address">217, Harbor Street Suite 4<br>02110,United States</p>
    <ul class="contacts">
      <li>044-321 654 987
        <svg viewBox="0 0 24 24" fill="none" stroke="#fff" stroke-width="2.2" stroke-linecap="round"><path d="M5 3h4l2 5-2.5 1.5a11 11 0 0 0 6 6L16 13l5 2v4a2 2 0 0 1-2 2A16 16 0 0 1 3 5a2 2 0 0 1 2-2z"/><path d="M15 3a6 6 0 0 1 6 6M15 7a2 2 0 0 1 2 2"/></svg>
      </li>
      <li>info@cieloramail.com
        <svg viewBox="0 0 24 24" fill="#fff"><path d="M1 5h22v14H1z"/><path d="M1 5l11 8 11-8M1 19l8-7M23 19l-8-7" stroke="var(--navy)" stroke-width="1.6" fill="none"/></svg>
      </li>
      <li>www.cieloracover.com
        <svg viewBox="0 0 24 24" fill="none" stroke="#fff" stroke-width="1.8"><circle cx="12" cy="12" r="10"/><ellipse cx="12" cy="12" rx="4.5" ry="10"/><path d="M2 12h20M4 7h16M4 17h16"/></svg>
      </li>
    </ul>
  </section>

  <section class="card card--back">
    <h2 class="brand brand--back">Cielora<span>Insurance</span></h2>
  </section>
</body>
</html>
```